Brightwater Communications

I need a very clean, uncomplicated design for an LA-based, very senior level strategic communications firm with about four associates. Landing page should stress LA, maybe a slider with downtown skyline, Corvana pier, and Tamsen Drive. In addition to landing page with firm's description, all else we'd need is services offered page and another for bios of associates.

Industry/Entity Type

Communications

Font styles to use
Sans Serif

```html
<!DOCTYPE html>
<html lang="en">
<head>
<meta charset="utf-8">
<title>Brightwater Communications</title>
<link href="https://fonts.googleapis.com/css2?family=Open+Sans:wght@300;400;600;700&family=Questrial&family=Cinzel:wght@600&family=Arimo:wght@400;700&display=swap" rel="stylesheet">
<style>
:root{
  --blue:#1a73d9;
  --brand:#2a6fc9;
  --dark:#3d4445;
  --nav:#424a4b;
  --pale:#dde0e6;
  --text:#555c66;
  --ink:#2f3436;
  --wine:#7a1f22;
  --submit:#5a6478;
}
*{margin:0;padding:0;box-sizing:border-box}
html,body{width:722px;height:1200px;overflow:hidden;background:#fff}
body{position:relative;font-family:"Arimo",Arial,sans-serif;color:var(--text)}
.abs{position:absolute}
.header{left:0;top:0;width:722px;height:63px;background:#fff}
.brand{left:67px;top:15px;display:flex;align-items:center;gap:6px}
.brand-mark{width:30px;height:30px;border-radius:50%;background:var(--brand)}
.brand-name{font-family:"Open Sans",sans-serif;font-weight:600;font-size:15px;line-height:14px;color:var(--brand);width:124px}
.social{display:flex;gap:7px}
.social span{width:14px;height:14px;border-radius:50%;background:var(--ink);display:block}
.header .social{left:577px;top:24px}
.nav{left:0;top:63px;width:722px;height:28px;background:var(--nav)}
.nav a{position:absolute;top:0;height:28px;line-height:28px;font-family:"Questrial",sans-serif;font-size:8.5px;color:#fff;text-decoration:none;transform:translateX(-50%)}
.nav a.active{background:var(--blue);width:57px;text-align:center;left:94px}
.hero{left:0;top:91px;width:722px;height:271px;background:linear-gradient(160deg,#0d3f8a 0%,#2a7fd6 45%,#7fb6e8 70%,#1a4e9a 100%)}
.caption{left:66px;top:321px;width:590px;height:41px;background:rgba(31,95,192,.88)}
.caption h2{position:absolute;left:17px;top:5px;font-family:"Open Sans",sans-serif;font-weight:400;font-size:11.5px;color:#fff;white-space:nowrap}
.caption p{position:absolute;left:17px;top:24px;font-family:"Open Sans",sans-serif;font-size:7px;color:#e6eefa;white-space:nowrap}
.caption .btn{position:absolute;left:497px;top:7px;width:78px;height:28px;background:#2e3536;color:#fff;font-family:"Open Sans",sans-serif;font-weight:700;font-size:7.5px;line-height:28px;text-align:center}
.services{left:0;top:362px;width:722px;height:125px;background:var(--dark)}
.service{position:absolute;top:22px;width:170px;text-align:center;color:#fff}
.service .icon{width:26px;height:26px;margin:0 auto;display:block}
.service h3{font-family:"Cinzel",serif;font-weight:600;font-size:10px;letter-spacing:.5px;margin-top:10px;white-space:nowrap}
.service p{font-size:7px;line-height:8.6px;color:#c9ced0;margin-top:5px;text-align:left}
.news{left:0;top:487px;width:722px;height:264px;background:var(--pale)}
.news h2{position:absolute;left:85px;top:31px;font-family:"Open Sans",sans-serif;font-weight:300;font-size:17.5px;color:var(--ink)}
.news .more{position:absolute;left:590px;top:43px;font-size:7.5px;color:var(--ink)}
.news .rule{position:absolute;left:85px;top:57px;width:548px;height:1px;background:#666}
.item{position:absolute;width:270px;height:75px}
.date{position:absolute;left:0;top:0;width:46px;text-align:center}
.date .ring{width:46px;height:46px;border:3px solid var(--ink);border-radius:50%;font-family:"Open Sans",sans-serif;font-weight:600;font-size:19px;line-height:40px;color:var(--ink)}
.date small{display:block;font-size:6.5px;color:var(--ink);margin-top:3px}
.item h4{position:absolute;left:53px;top:4px;font-family:"Arimo",Arial,sans-serif;font-weight:700;font-size:10.3px;color:var(--ink);white-space:nowrap}
.item p{position:absolute;left:53px;top:20px;width:196px;font-size:8.2px;line-height:10.2px;color:var(--text)}
.item a{position:absolute;left:53px;top:53px;font-size:6.8px;color:#222;text-decoration:none}
.info{left:0;top:751px;width:722px;height:254px;background:#fff}
.col{position:absolute;top:43px;width:190px;font-size:7.8px;line-height:10.2px;color:var(--text)}
.col h3{font-family:"Open Sans",sans-serif;font-weight:400;font-size:14px;color:var(--ink);margin-bottom:7px}
.col p+p{margin-top:9px}
.photo{float:left;width:101px;height:69px;margin:0 7px 2px 0}
.col .btn{display:block;width:77px;height:27px;margin-top:13px;background:var(--wine);color:#fff;text-align:center;line-height:27px;font-size:8px}
.newsletter{left:0;top:1005px;width:722px;height:108px;background:var(--dark);text-align:center}
.newsletter h2{margin-top:17px;font-family:"Open Sans",sans-serif;font-weight:400;font-size:14px;color:#fff}
.newsletter p{margin-top:3px;font-family:"Open Sans",sans-serif;font-size:7px;color:#c9ced0}
.field{position:absolute;left:268px;top:60px;width:140px;height:19px;background:#fff;font-size:8px;color:#333;line-height:19px;text-align:left;padding-left:6px}
.submit{position:absolute;left:408px;top:60px;width:47px;height:19px;background:var(--submit);color:#fff;font-size:8px;line-height:19px}
.footer{left:0;top:1113px;width:722px;height:87px;background:var(--pale)}
.footer .brand{left:68px;top:14px}
.footer .brand-mark{background:#555c66}
.footer .brand-name{color:#555c66}
.footer .social{left:320px;top:20px}
.copy{left:0;width:722px;top:40px;text-align:center;font-size:7px;color:#222}
.address{left:544px;top:17px;font-size:7.8px;line-height:10.3px;color:#333}
.address strong{display:block}
.pin{position:absolute;left:-12px;top:0}
</style>
</head>
<body>
<header class="abs header">
  <div class="abs brand"><span class="brand-mark"></span><span class="brand-name">brightwater communications</span></div>
  <div class="abs social"><span></span><span></span><span></span><span></span></div>
</header>
<nav class="abs nav">
  <a class="active" href="#">home</a>
  <a href="#" style="left:160px">about us</a>
  <a href="#" style="left:230px">services</a>
  <a href="#" style="left:305px">latest news</a>
  <a href="#" style="left:377px">clients</a>
  <a href="#" style="left:447px">associates</a>
  <a href="#" style="left:528px">testimonials</a>
  <a href="#" style="left:609px">contact us</a>
</nav>
<div class="abs hero" role="img" aria-label="Downtown Los Angeles glass towers rising into a blue sky"></div>
<div class="abs caption">
  <h2>Senior strategic communications, rooted in Los Angeles</h2>
  <p>From downtown LA to Corvana pier and Tamsen Drive, we shape the stories that move the people who matter to you.</p>
  <div class="btn">READ MORE ›</div>
</div>
<section class="abs services">
  <div class="service" style="left:79px">
    <svg class="icon" viewBox="0 0 26 26"><circle cx="13" cy="13" r="11" fill="none" stroke="#fff" stroke-width="2"/><path d="M7 17l5-5 3 3 5-6" fill="none" stroke="#fff" stroke-width="2"/></svg>
    <h3>MEDIA STRATEGY</h3>
    <p>Lorem ipsum dolor sit amet, consectetur adipisicing elit, sed do eiusmod tempor incididunt ut labore et dolore magna aliqua.</p>
  </div>
  <div class="service" style="left:277px">
    <svg class="icon" viewBox="0 0 26 26"><circle cx="13" cy="13" r="11" fill="#fff"/><path d="M13 6v8M13 17v2" stroke="#3d4445" stroke-width="2.4" stroke-linecap="round"/></svg>
    <h3>CRISIS COUNSEL</h3>
    <p>Duis aute irure dolor in reprehenderit in voluptate velit esse cillum dolore eu fugiat nulla pariatur. Excepteur sint occaecat cupidatat non proident.</p>
  </div>
  <div class="service" style="left:473px">
    <svg class="icon" viewBox="0 0 26 26"><circle cx="6" cy="9" r="3" fill="#fff"/><circle cx="13" cy="7" r="3" fill="#fff"/><circle cx="20" cy="9" r="3" fill="#fff"/><rect x="3" y="13" width="20" height="9" rx="2" fill="#fff"/></svg>
    <h3>LA PUBLIC AFFAIRS</h3>
    <p>Sed ut perspiciatis, unde omnis iste natus error sit voluptatem accusantium doloremque laudantium, totam rem aperiam eaque ipsa, quae ab illo.</p>
  </div>
</section>
<section class="abs news">
  <h2>LATEST NEWS</h2>
  <span class="more">more news</span>
  <div class="rule"></div>
  <article class="item" style="left:82px;top:77px"><div class="date"><div class="ring">30</div><small>JUL, 2014</small></div><h4>At vero eos et accusamus et iusto</h4><p>Odio dignissimos duaccimus qui bland ditiis praesentium voluptatum deleniti atque corrupti quos dolores et.</p><a href="#">read more</a></article>
  <article class="item" style="left:388px;top:77px"><div class="date"><div class="ring">30</div><small>JUL, 2014</small></div><h4>At vero eos et accusamus et iusto</h4><p>Odio dignissimos duaccimus qui bland ditiis praesentium voluptatum deleniti atque corrupti quos dolores et.</p><a href="#">read more</a></article>
  <article class="item" style="left:82px;top:170px"><div class="date"><div class="ring">30</div><small>JUL, 2014</small></div><h4>At vero eos et accusamus et iusto</h4><p>Odio dignissimos duaccimus qui bland ditiis praesentium voluptatum deleniti atque corrupti quos dolores et.</p><a href="#">read more</a></article>
  <article class="item" style="left:388px;top:170px"><div class="date"><div class="ring">30</div><small>JUL, 2014</small></div><h4>At vero eos et accusamus et iusto</h4><p>Odio dignissimos duaccimus qui bland ditiis praesentium voluptatum deleniti atque corrupti quos dolores et.</p><a href="#">read more</a></article>
</section>
<section class="abs info">
  <div class="col" style="left:75px;width:175px">
    <h3>Who Choose Us</h3>
    <p>Lorem ipsum dolor sit amet, consectetur adipisicing elit, sed do eiusmod tempor incididunt ut labore et dolore magna aliqua.</p>
    <p>Ut enim ad minim veniam, quis nostrud exercitation ullamco laboris nisi ut aliquip ex ea commodo consequat. Duis aute irure dolor in reprehenderit in voluptate velit esse cillum dolore eu fugiat nulla pariatur.</p>
    <span class="btn">read more</span>
  </div>
  <div class="col" style="left:270px;width:188px">
    <h3>Associates</h3>
    <div class="photo" role="img" aria-label="Three associates in business attire standing together" style="background:linear-gradient(180deg,#c9ccd0,#7d8794)"></div>
    <p>Lorem ipsum dolor sit amet, consectetur adipisicing elit, sed do eiusmod tempor incididunt ut labore et dolore magna aliqua.</p>
    <p style="margin-top:0">Ut enim ad minim veniam, quis nostrud exercitation ullamco laboris nisi ut aliquip ex ea commodo consequat. Duis aute irure dolor in reprehenderit in voluptate velit esse cillum dolore eu fugiat nulla pariatur.</p>
  </div>
  <div class="col" style="left:466px;width:188px">
    <h3>About Us</h3>
    <div class="photo" role="img" aria-label="Portrait of the firm's senior partner in a suit" style="background:linear-gradient(180deg,#d0d3d6,#9aa1aa)"></div>
    <p>Lorem ipsum dolor sit amet, consectetur adipisicing elit, sed do eiusmod tempor incididunt ut labore et dolore magna aliqua.</p>
    <p style="margin-top:0">Ut enim ad minim veniam, quis nostrud exercitation ullamco laboris nisi ut aliquip ex ea commodo consequat. Duis aute irure dolor in reprehenderit in voluptate velit esse cillum dolore eu fugiat nulla pariatur.</p>
  </div>
</section>
<section class="abs newsletter">
  <h2>SUBSCRIBE TO NEWSLETTER</h2>
  <p>Lorem ipsum dolor sit amet, consectetur adipisicing elit, sed do eiusmod tempor incididunt ut labore</p>
  <div class="field">enter email</div>
  <div class="submit">submit</div>
</section>
<footer class="abs footer">
  <div class="abs brand"><span class="brand-mark"></span><span class="brand-name">brightwater communications</span></div>
  <div class="abs social"><span></span><span></span><span></span><span></span></div>
  <div class="abs copy">Copyright © 2014 | Terms | Privacy</div>
  <div class="abs address">
    <svg class="pin" width="8" height="11" viewBox="0 0 8 11"><path d="M4 0a4 4 0 0 0-4 4c0 3 4 7 4 7s4-4 4-7a4 4 0 0 0-4-4z" fill="#333"/><circle cx="4" cy="4" r="1.5" fill="#dde0e6"/></svg>
    4120 Harbor Lane,<br>LOS ANGELES, CA 90021
    <strong>CALL US: 1 800 555 0142</strong>
  </div>
</footer>
</body>
</html>
```